Sponsors Ad for the WCLGA 75th Anniversary Gala

This ad is to congratulate the awardees and the WCLGA for its 75th anniversary. Harborline is a sponsor and we get a full screen ad as part of our sponsorship. I have attached the spec sheet for the full screen ad, a PDF of the gala website with the people being honored and the information of that they are celebrating the 75th anniversary, I also attached my logo. My website is www.harborlinetq.example if you want to get any information from that. See sample ads of others from past years uploaded.

Target Market(s)

Attendees at the Gala (attorneys will be attending)

Industry/Entity Type

legal

Requirements
Must have
• Congratulations to the award recipients and the WCLGA for 75th Anniv.
Nice to have
• Reference to the high standard and quality of the work done by Harborline but subtle as this is not the primary purpose.
Should not have
• dates and times

```html
<!DOCTYPE html>
<html lang="en">
<head>
<meta charset="utf-8">
<title>Harborline – WCLGA 75th Anniversary Gala Sponsor Ad</title>
<link rel="stylesheet" href="https://fonts.googleapis.com/css2?family=Questrial&display=swap">
<style>
  :root {
    --navy: #17375a;
    --navy-deep: #13304f;
    --gold: #c39a36;
    --white: #ffffff;
    --footer-grey: #e8e8e9;
    --photo-dark: #3a4450;
    --photo-light: #b9c0c6;
  }
  * { margin: 0; padding: 0; box-sizing: border-box; }
  html, body { width: 675px; height: 1200px; overflow: hidden; background: var(--white); }
  body { font-family: "Questrial", sans-serif; color: var(--navy); }
  .ad { position: relative; width: 675px; height: 1200px; overflow: hidden; }

  .hero-photo {
    position: absolute; left: 0; top: 0; width: 675px; height: 459px;
    background:
      linear-gradient(180deg, rgba(19,48,79,0) 62%, rgba(19,48,79,0.92) 100%),
      linear-gradient(120deg, var(--photo-light) 0%, #8d949b 35%, var(--photo-dark) 70%, #1f2f4a 100%);
  }
  .congrats {
    position: absolute; left: 62px; top: 384px; width: 560px;
    font-size: 18px; line-height: 24px; color: var(--white);
  }
  .congrats strong { font-weight: 400; color: var(--gold); }

  .headline-band {
    position: absolute; left: 0; top: 459px; width: 675px; height: 175px;
    background: var(--navy);
  }
  .headline {
    position: absolute; left: 62px; top: 14px;
    font-size: 68px; line-height: 57px; font-weight: 400;
    color: var(--gold); letter-spacing: 0.5px;
  }
  .subline {
    position: absolute; left: 62px; top: 140px;
    font-size: 13.2px; color: var(--white); white-space: nowrap;
  }

  .rule-gold { position: absolute; left: 0; width: 675px; background: var(--gold); }
  .rule-top { top: 634px; height: 14px; }
  .rule-bottom { top: 1164px; height: 12px; }

  .services { position: absolute; left: 0; top: 648px; width: 675px; height: 391px; background: var(--white); }
  .service { position: absolute; width: 200px; text-align: center; }
  .service-icon {
    display: block; width: 77px; height: 77px; margin: 0 auto 8px;
    background: var(--navy);
  }
  .service-icon svg { width: 77px; height: 77px; }
  .service-label { font-size: 22px; line-height: 23px; color: var(--navy); }

  .footer { position: absolute; left: 0; top: 1039px; width: 675px; height: 125px; background: var(--footer-grey); }
  .brand { position: absolute; left: 64px; top: 44px; display: flex; align-items: center; gap: 14px; }
  .brand-mark { width: 34px; height: 34px; background: var(--navy); }
  .brand-name { font-size: 38px; line-height: 40px; color: var(--navy); }
  .site { position: absolute; left: 392px; top: 48px; font-size: 24px; line-height: 30px; color: var(--navy); white-space: nowrap; }

  .base-band { position: absolute; left: 0; top: 1176px; width: 675px; height: 24px; background: var(--navy); }
</style>
</head>
<body>
<div class="ad">
  <div class="hero-photo" role="img" aria-label="Photo of two professionals reviewing a tablet together in a bright office"></div>
  <p class="congrats">Congratulations to this year’s honorees and to the <strong>WCLGA</strong> on its <strong>75th Anniversary</strong>.</p>

  <section class="headline-band">
    <h1 class="headline">Precision. Insight.<br>Confidence.</h1>
    <p class="subline">Trusted valuation expertise for businesses, legal professionals, and financial stakeholders.</p>
  </section>
  <div class="rule-gold rule-top"></div>

  <section class="services">
    <div class="service" style="left:32px; top:36px;">
      <span class="service-icon"><svg viewBox="0 0 77 77" fill="none" stroke="#fff" stroke-width="1.6"><circle cx="40" cy="32" r="9"/><path d="M36 22l4-4 4 4"/><path d="M22 52h8l10 3 14-6"/><rect x="18" y="46" width="5" height="12"/></svg></span>
      <div class="service-label">Estate+Gift<br>Reporting</div>
    </div>
    <div class="service" style="left:237px; top:36px;">
      <span class="service-icon"><svg viewBox="0 0 77 77" fill="none" stroke="#fff" stroke-width="1.6"><path d="M24 20h20l6 6v30H24z"/><path d="M29 48v-6M34 48v-10M39 48v-8"/><circle cx="51" cy="50" r="5"/></svg></span>
      <div class="service-label">Financial<br>Options &amp;<br>Transaction<br>Supports</div>
    </div>
    <div class="service" style="left:441px; top:36px;">
      <span class="service-icon"><svg viewBox="0 0 77 77" fill="none" stroke="#fff" stroke-width="1.6"><circle cx="28" cy="32" r="4"/><circle cx="38" cy="28" r="4"/><circle cx="48" cy="32" r="4"/><path d="M20 46v-6h16v6M40 46v-6h16v6"/><circle cx="38" cy="46" r="6"/><path d="M35 46l2 2 4-4"/></svg></span>
      <div class="service-label">ESOP<br>Advisory</div>
    </div>
    <div class="service" style="left:30px; top:185px;">
      <span class="service-icon"><svg viewBox="0 0 77 77" fill="none" stroke="#fff" stroke-width="1.6"><path d="M22 20h24v36H22z"/><path d="M27 28h14M27 34h14M27 40h10"/><path d="M44 44l10 10M42 46l6-6"/></svg></span>
      <div class="service-label">Litigation<br>Support &amp;<br>Forensics</div>
    </div>
    <div class="service" style="left:237px; top:230px;">
      <span class="service-icon"><svg viewBox="0 0 77 77" fill="none" stroke="#fff" stroke-width="1.6"><path d="M34 28a12 12 0 1 0 12 12H34z"/><circle cx="49" cy="26" r="7"/><path d="M49 22v8"/></svg></span>
      <div class="service-label">Portfolio &amp; Asset<br>Valuations</div>
    </div>
    <div class="service" style="left:442px; top:187px;">
      <span class="service-icon"><svg viewBox="0 0 77 77" fill="none" stroke="#fff" stroke-width="1.6"><circle cx="38" cy="38" r="10"/><path d="M38 32v12"/><path d="M24 30a16 16 0 0 1 26-8l4-2M52 46a16 16 0 0 1-26 8l-4 2"/></svg></span>
      <div class="service-label">Transaction<br>&amp; Reporting<br>Valuations</div>
    </div>
  </section>

  <footer class="footer">
    <div class="brand">
      <span class="brand-mark"></span>
      <span class="brand-name">Harborline</span>
    </div>
    <div class="site">harborlinetq.example</div>
  </footer>
  <div class="rule-gold rule-bottom"></div>
  <div class="base-band"></div>
</div>
</body>
</html>
```